Satchel & Compass needs new business card design

I need a new business card design. I'm looking for out-of-the-box design which represents the freedom of being a location independent entrepreneur.
I offer coaching, retreats and trips.
I would like to see designs with and without the photo.
Colors I use are black (#000000), green (#25A796) and brown (#D7C38C)
Website satchelandcompass.com

Target Market(s)

location independent entrepreneurs, digital nomads, people looking to swap the 9 to 5 for a lifestyle business

Industry/Entity Type

Business

Contact Information for Business Card

Petra Varga
Your Lifestyle Business Coach, Retreat & Trip Leader
http://satchelandcompass.com
hello@satchelandcompass.com
Live a life you don't need a holiday from

Font styles to use
Serif
Sans Serif

Requirements
Must have
• One side should contain only the logo. I would also consider having the "Live a life you don't need a holiday from" on that side too (depending on how it looks)
• Please show both sides on the designs.

```html
<!DOCTYPE html>
<html lang="en">
<head>
<meta charset="utf-8">
<title>Satchel &amp; Compass — Business Card</title>
<link rel="stylesheet" href="https://fonts.googleapis.com/css2?family=Arimo:wght@400;700&display=swap">
<style>
  :root {
    --page-bg: #d9d9d9;
    --card-bg: #f4f4f4;
    --teal: #35ae9f;
    --ink: #111111;
    --ink-soft: #2a2a2a;
    --card-shadow: 0 10px 28px rgba(0,0,0,0.22);
  }
  * { margin: 0; padding: 0; box-sizing: border-box; }
  html, body { width: 1200px; height: 864px; overflow: hidden; }
  body {
    background: var(--page-bg);
    font-family: "Arimo", Arial, sans-serif;
    color: var(--ink);
    position: relative;
  }
  .card {
    position: absolute;
    width: 620px;
    height: 354px;
    background: var(--card-bg);
    box-shadow: var(--card-shadow);
    overflow: hidden;
  }

  /* Logo side */
  .card--logo { left: 520px; top: 60px; }
  .card--logo .brand-name {
    position: absolute;
    left: 0; right: 0; top: 112px;
    text-align: center;
    font-size: 44px;
    font-weight: 700;
    letter-spacing: 1px;
    color: var(--ink);
  }
  .card--logo .tagline {
    position: absolute;
    left: 0; right: 0; top: 226px;
    text-align: center;
    font-size: 19px;
    color: var(--ink);
  }

  /* Contact side */
  .card--contact { left: 60px; top: 450px; }
  .card-swoosh { position: absolute; inset: 0; width: 100%; height: 100%; }
  .card--contact .brand-name {
    position: absolute;
    right: 34px; top: 66px;
    font-size: 30px;
    font-weight: 700;
    letter-spacing: 0.5px;
    color: var(--ink);
    white-space: nowrap;
  }
  .holder {
    position: absolute;
    left: 22px; bottom: 52px;
    color: var(--ink-soft);
    white-space: nowrap;
  }
  .holder-name {
    font-size: 22px;
    font-weight: 700;
    margin-bottom: 4px;
    color: #1f1f1f;
  }
  .holder-role {
    font-size: 13px;
    line-height: 1.25;
  }
  .contact-list {
    position: absolute;
    right: 26px; bottom: 40px;
    list-style: none;
    text-align: right;
  }
  .contact-item {
    display: flex;
    align-items: center;
    justify-content: flex-end;
    gap: 14px;
    font-size: 20px;
    line-height: 1;
    margin-top: 12px;
    white-space: nowrap;
  }
  .contact-icon {
    width: 22px; height: 22px;
    background: var(--ink);
    display: inline-flex;
    align-items: center;
    justify-content: center;
  }
</style>
</head>
<body>

  <section class="card card--logo" aria-label="Business card, logo side">
    <p class="brand-name">Satchel &amp; Compass</p>
    <p class="tagline">Live a life you don't need a holiday from</p>
  </section>

  <section class="card card--contact" aria-label="Business card, contact side">
    <svg class="card-swoosh" viewBox="0 0 620 354" preserveAspectRatio="none" aria-hidden="true">
      <path d="M0 0 H272 C190 90 186 260 266 354 H0 Z" fill="var(--teal)"/>
      <path d="M292 0 C205 90 200 260 283 354 L292 354 C225 260 232 90 306 0 Z" fill="var(--ink)"/>
    </svg>

    <p class="brand-name">Satchel &amp; Compass</p>

    <div class="holder">
      <p class="holder-name">Petra Varga</p>
      <p class="holder-role">Your Lifestyle Business Coach,<br>Retreat &amp; Trip Leader</p>
    </div>

    <ul class="contact-list">
      <li class="contact-item">
        <span>hello@satchelandcompass.com</span>
        <span class="contact-icon">
          <svg width="16" height="12" viewBox="0 0 16 12" aria-hidden="true">
            <rect x="0.75" y="0.75" width="14.5" height="10.5" fill="none" stroke="#fff" stroke-width="1.5"/>
            <path d="M1 1 L8 7 L15 1" fill="none" stroke="#fff" stroke-width="1.5"/>
          </svg>
        </span>
      </li>
      <li class="contact-item">
        <span>http://satchelandcompass.com</span>
        <span class="contact-icon">
          <svg width="16" height="16" viewBox="0 0 16 16" aria-hidden="true">
            <circle cx="8" cy="8" r="6.5" fill="none" stroke="#fff" stroke-width="1.5"/>
            <ellipse cx="8" cy="8" rx="2.8" ry="6.5" fill="none" stroke="#fff" stroke-width="1.2"/>
            <path d="M1.5 8 H14.5" stroke="#fff" stroke-width="1.2"/>
          </svg>
        </span>
      </li>
    </ul>
  </section>

</body>
</html>
```